" Sou médica dermatologista sócia de uma biomédica. Pretendemos dar aulas teóricas e práticas de procedimentos como toxina botulínica, preenchedores, peeling químico, lasers etc "

```html
<!DOCTYPE html>
<html lang="pt-BR">
<head>
<meta charset="utf-8">
<title>Derma Ensino – Cursos</title>
<link href="https://fonts.googleapis.com/css2?family=Open+Sans:ital,wght@0,400;0,600;0,700;1,400;1,600;1,700&family=Oswald:wght@400;500;600&display=swap" rel="stylesheet">
<style>
:root{
  --green:#3f8a2b;
  --green-dark:#2f6e1f;
  --green-light:#8cc06b;
  --hero-a:#5e9c3c;
  --hero-b:#a9cf86;
  --text:#555;
  --muted:#888;
  --line:#ddd;
  --panel:#f3f3f3;
  --footer:#ececec;
  --white:#fff;
}
*{box-sizing:border-box;margin:0;padding:0}
html,body{width:1200px;height:1200px;overflow:hidden;background:var(--white);font-family:"Open Sans",sans-serif;color:var(--text);position:relative}
.wrap{width:760px;margin:0 auto;position:relative}

/* header / hero */
.hero{height:252px;position:relative;background:linear-gradient(180deg,var(--hero-a),var(--hero-b) 70%,#e6f0dc);overflow:hidden}
.hero-photo{position:absolute;inset:0;background:radial-gradient(ellipse at 30% 60%,rgba(255,255,255,.25),transparent 60%),radial-gradient(ellipse at 80% 40%,rgba(40,90,20,.35),transparent 60%)}
.topnav{position:absolute;top:0;left:0;right:0;height:56px;background:rgba(30,90,20,.55)}
.topnav .wrap{display:flex;justify-content:space-between;height:56px;align-items:center}
.topnav ul{display:flex;list-style:none}
.topnav li{font-family:"Oswald",sans-serif;font-weight:500;color:var(--white);font-size:12px;padding:6px 8px;letter-spacing:.3px;white-space:nowrap}
.topnav li.active{border-bottom:3px solid var(--white)}
.brand{position:absolute;left:50%;top:-70px;transform:translateX(-50%);width:210px;height:140px;background:var(--white);border-radius:0 0 105px 105px;display:flex;align-items:flex-end;justify-content:center;padding-bottom:30px;gap:7px}
.brand-dot{width:10px;height:10px;border-radius:50%;background:var(--green)}
.brand-name{font-family:"Oswald",sans-serif;font-weight:600;font-size:20px;color:var(--green-dark);letter-spacing:.5px;white-space:nowrap}
.hero-title{position:absolute;top:176px;left:0;right:0;text-align:center;font-family:"Oswald",sans-serif;font-weight:500;font-size:24px;color:var(--white);letter-spacing:1px}
.hero-curve{position:absolute;bottom:-1px;left:0;width:100%}

/* course tabs */
.tabs{display:flex;justify-content:space-between;border-top:1px solid var(--line);border-bottom:1px solid var(--line);margin-top:28px;padding:9px 4px}
.tabs span{font-size:7.5px;font-weight:600;text-transform:uppercase;color:#666;white-space:nowrap}
.tabs span.active{color:var(--green)}

.course{margin-top:14px;border:1px solid var(--line);border-radius:4px;display:flex;padding:10px 14px 22px;background:linear-gradient(90deg,var(--panel) 0 170px,var(--white) 170px)}
.course-side{width:160px;flex:none}
.course-photo{width:96px;height:86px;border-radius:6px;background:linear-gradient(135deg,#f1d9c6,#c99d86);margin-bottom:14px}
.course-side dt{font-size:10px;font-weight:700;color:var(--green-dark);margin-bottom:7px}
.course-side dt.active{color:var(--green)}
.course-body{padding-left:20px}
.course-body h3{font-style:italic;font-weight:700;font-size:14px;color:var(--green)}
.course-body h4{font-weight:700;font-size:13px;color:#333;margin:4px 0 6px}
.course-body li{font-size:9.5px;list-style:none;line-height:1.38}
.course-btn{display:block;margin:-12px auto 0;width:190px;text-align:center;background:var(--green);color:var(--white);font-size:9px;font-weight:700;padding:7px 0;border-radius:2px;position:relative}

/* calendar */
.cal{display:flex;margin-top:34px;align-items:flex-start}
.cal-intro{width:200px;flex:none}
.sec-title{font-style:italic;font-weight:700;color:var(--green);font-size:14px;display:flex;align-items:center;gap:8px}
.sec-title::before{content:"";width:8px;height:8px;background:var(--green);display:inline-block}
.cal-intro p{font-size:9.5px;color:var(--muted);margin-top:10px;line-height:1.5;padding-left:16px}
.cal-cards{display:flex;gap:22px;margin-left:auto}
.cal-card{display:flex;gap:10px;width:170px;align-items:center}
.cal-card small{display:block;font-style:italic;font-size:10px;color:var(--green-light)}
.cal-card strong{display:block;font-family:"Oswald",sans-serif;font-weight:500;font-size:27px;color:var(--green);line-height:1.05;white-space:nowrap}
.cal-card em{font-size:10px;color:var(--green-light)}
.other{display:flex;align-items:center;margin-top:24px;border-top:1px solid var(--line);border-bottom:1px solid var(--line);padding:10px 0}
.other h5{font-style:italic;font-size:13px;font-weight:600;color:var(--muted);width:200px;flex:none}
.other-items{display:flex;gap:46px}
.other-item{display:flex;align-items:center;gap:6px}
.other-item b{font-family:"Oswald",sans-serif;font-weight:500;font-size:13px;color:var(--green-dark)}
.other-item i{display:block;font-size:8px;color:var(--muted)}

/* info */
.info{margin-top:34px}
.info-cols{display:flex;gap:40px;margin-top:16px;font-size:9.5px;line-height:1.5}
.info-cols div{flex:1}
.info-cols p{margin-bottom:12px}
.info-note{text-align:center;font-size:9.5px;font-weight:700;color:#333;margin-top:2px;line-height:1.45}

/* footer */
.footer{position:absolute;left:0;right:0;top:1042px;height:158px;background:var(--footer);border-top:6px solid var(--green)}
.footer .wrap{display:flex;gap:30px;padding-top:14px}
.foot-col{flex:1;font-size:9px;line-height:1.5}
.foot-col h6{font-size:11px;font-weight:700;text-transform:uppercase;color:#444;margin-bottom:10px;display:flex;align-items:center;gap:6px}
.foot-col h6::before{content:"";width:7px;height:7px;background:var(--green)}
.socials{display:flex;gap:6px;margin-bottom:8px}
.socials span{width:20px;height:20px;border-radius:3px;background:var(--green)}
.socials span.b{width:58px;background:#bbb}
.contact-row{display:flex;gap:18px}
.contact-row b{display:block;color:var(--green-dark)}
.bottom{position:absolute;bottom:0;left:0;right:0;height:24px;background:#ddd;font-size:8px;color:var(--muted);display:flex;align-items:center;justify-content:center}
</style>
</head>
<body>

<header class="hero">
  <div class="hero-photo" role="img" aria-label="Foto de fundo em tons verdes com tratamento estético"></div>
  <nav class="topnav">
    <div class="wrap">
      <ul><li>HOME</li><li>INSTITUCIONAL</li><li>CORPO DOCENTE</li></ul>
      <ul><li class="active">CURSOS</li><li>GALERIA DE FOTOS</li><li>CONTATO</li></ul>
    </div>
  </nav>
  <div class="brand"><span class="brand-dot"></span><span class="brand-name">DERMA ENSINO</span></div>
  <h1 class="hero-title">CURSOS</h1>
  <svg class="hero-curve" viewBox="0 0 1200 40" height="40" preserveAspectRatio="none"><path d="M0 40 Q600 -10 1200 40 Z" fill="#fff"/></svg>
</header>

<main class="wrap">
  <div class="tabs">
    <span>Toxina Botulínica</span><span>Preenchimento</span><span>Peelings</span><span>Prescrição</span>
    <span class="active">Intradermoterapia e Microagulhamento</span><span>Laser</span><span>Atualização em Morfologia</span><span>Patologia na Estética</span>
  </div>

  <section class="course">
    <dl class="course-side">
      <div class="course-photo" role="img" aria-label="Foto de aplicação com microagulhamento"></div>
      <dt>Objetivo</dt><dt class="active">Conteúdo Programático</dt><dt>Investimento</dt><dt>Forma de Pagamento</dt>
    </dl>
    <div class="course-body">
      <h3>Microagulhamento</h3>
      <h4>Conteúdo Programático</h4>
      <ul>
        <li>• Indicações;</li><li>• Efeitos Colaterais;</li><li>• Contra Indicações;</li><li>• Estrutura da pele;</li>
        <li>• Associação com outros tratamentos;</li><li>• Prática;</li><li>• Protocolos e Técnicas de aplicação;</li>
        <li>• Sequela de acne;</li><li>• Alopecia;</li><li>• Flacidez Corporal;</li><li>• Estrias;</li><li>• Flacidez e Rugas.</li>
      </ul>
    </div>
  </section>
  <span class="course-btn">DÚVIDAS DO CURSO? INSCREVA-SE</span>

  <section class="cal">
    <div class="cal-intro">
      <h2 class="sec-title">CALENDÁRIO DE AULAS</h2>
      <p>Confira suas datas de aulas e não perca a chance de ficar de fora dessa turma especial.</p>
    </div>
    <div class="cal-cards">
      <div class="cal-card">
        <svg width="34" height="34" viewBox="0 0 34 34"><rect x="2" y="5" width="30" height="27" rx="3" fill="#3f8a2b"/><rect x="8" y="1" width="4" height="8" rx="1" fill="#2f6e1f"/><rect x="22" y="1" width="4" height="8" rx="1" fill="#2f6e1f"/><g fill="#fff"><rect x="6" y="13" width="5" height="4"/><rect x="14.5" y="13" width="5" height="4"/><rect x="23" y="13" width="5" height="4"/><rect x="6" y="21" width="5" height="4"/><rect x="14.5" y="21" width="5" height="4"/><rect x="23" y="21" width="5" height="4"/></g></svg>
        <div><small>Dia de início</small><strong>20, 21 e 22</strong><em>novembro</em></div>
      </div>
      <div class="cal-card">
        <svg width="34" height="34" viewBox="0 0 34 34"><rect x="2" y="5" width="30" height="27" rx="3" fill="#3f8a2b"/><rect x="8" y="1" width="4" height="8" rx="1" fill="#2f6e1f"/><rect x="22" y="1" width="4" height="8" rx="1" fill="#2f6e1f"/><g fill="#fff"><rect x="6" y="13" width="5" height="4"/><rect x="14.5" y="13" width="5" height="4"/><rect x="23" y="13" width="5" height="4"/><rect x="6" y="21" width="5" height="4"/><rect x="14.5" y="21" width="5" height="4"/><rect x="23" y="21" width="5" height="4"/></g></svg>
        <div><small>Dia de início</small><strong>01, 02 e 03</strong><em>dezembro</em></div>
      </div>
      <div class="cal-card">
        <svg width="34" height="34" viewBox="0 0 34 34"><rect x="2" y="5" width="30" height="27" rx="3" fill="#3f8a2b"/><rect x="8" y="1" width="4" height="8" rx="1" fill="#2f6e1f"/><rect x="22" y="1" width="4" height="8" rx="1" fill="#2f6e1f"/><g fill="#fff"><rect x="6" y="13" width="5" height="4"/><rect x="14.5" y="13" width="5" height="4"/><rect x="23" y="13" width="5" height="4"/><rect x="6" y="21" width="5" height="4"/><rect x="14.5" y="21" width="5" height="4"/><rect x="23" y="21" width="5" height="4"/></g></svg>
        <div><small>Dia de início</small><strong>22, 23 e 24</strong><em>janeiro</em></div>
      </div>
    </div>
  </section>

  <section class="other">
    <h5>Datas para outros estados »</h5>
    <div class="other-items">
      <div class="other-item"><svg width="16" height="16" viewBox="0 0 16 16"><rect x="1" y="3" width="14" height="12" rx="2" fill="#3f8a2b"/><rect x="3" y="7" width="10" height="6" fill="#fff"/></svg><div><b>11, 12 e 13</b><i>dezembro</i></div></div>
      <div class="other-item"><svg width="16" height="16" viewBox="0 0 16 16"><rect x="1" y="3" width="14" height="12" rx="2" fill="#3f8a2b"/><rect x="3" y="7" width="10" height="6" fill="#fff"/></svg><div><b>15, 16 e 17</b><i>dezembro</i></div></div>
      <div class="other-item"><svg width="16" height="16" viewBox="0 0 16 16"><rect x="1" y="3" width="14" height="12" rx="2" fill="#3f8a2b"/><rect x="3" y="7" width="10" height="6" fill="#fff"/></svg><div><b>08, 09 e 10</b><i>janeiro</i></div></div>
      <div class="other-item"><svg width="16" height="16" viewBox="0 0 16 16"><rect x="1" y="3" width="14" height="12" rx="2" fill="#3f8a2b"/><rect x="3" y="7" width="10" height="6" fill="#fff"/></svg><div><b>12, 13 e 14</b><i>janeiro</i></div></div>
    </div>
  </section>

  <section class="info">
    <h2 class="sec-title">MAIS INFORMAÇÕES</h2>
    <div class="info-cols">
      <div>
        <p><b>Público Alvo:</b> Profissionais da área da saúde.</p>
        <p>• Entrega de certificados válidos em todo território nacional, e podem constar nos currículos dos profissionais que frequentaram a carga horária mínima de noventa por cento do curso. Caso contrário, a certificação não será concedida sem direito a reembolso ao aluno ou reposição das aulas perdidas.</p>
        <p>Alunos que faltarem em grupo de no mínimo quinze pessoas devem remarcar suas aulas com antecedência e confirmar a participação com a coordenação.</p>
      </div>
      <div>
        <p>• Material didático.</p>
        <p>• Material clínico mínimo necessário para as práticas demonstrativas.</p>
        <p>Não consta brinde e o aluno deverá trazer seu próprio modelo e adquirir o material que será utilizado posteriormente. Possibilidade de curso em outro estado.</p>
      </div>
    </div>
    <p class="info-note">Para 2º dia de curso acompanhado somente com mínimo de 2 módulos e de 10 a 15 alunos. O profissional que organizar a infraestrutura local terá desconto nos cursos.</p>
  </section>
</main>

<footer class="footer">
  <div class="wrap">
    <div class="foot-col">
      <h6>Sobre nós</h6>
      <p>A Derma Ensino nasceu para atender a crescente demanda de profissionais da saúde pela capacitação prática em procedimentos estéticos, com aulas teóricas e práticas ministradas por especialistas, sempre com foco em segurança e resultado.</p>
    </div>
    <div class="foot-col">
      <h6>Redes sociais</h6>
      <div class="socials"><span></span><span></span><span></span><span class="b"></span><span class="b"></span></div>
      <div class="contact-row">
        <div><b>Atendimento</b>(21) 90000-1234</div>
        <div><b>E-mail</b>contato@dermaensino.com.br</div>
      </div>
    </div>
    <div class="foot-col">
      <h6>Nossa localização</h6>
      <p>Venha nos conhecer e saber mais sobre os nossos cursos.</p>
      <p><svg width="9" height="11" viewBox="0 0 9 11"><path d="M4.5 0a4 4 0 0 1 4 4c0 3-4 7-4 7S.5 7 .5 4a4 4 0 0 1 4-4z" fill="#3f8a2b"/><circle cx="4.5" cy="4" r="1.5" fill="#fff"/></svg> <b>Rua:</b> Rua das Acácias, 120 - Centro, São Paulo</p>
      <p><b>CEP:</b> 01234-567</p>
      <p>Veja nosso mapa de localização</p>
    </div>
  </div>
  <div class="bottom">© 2015 - Todos os direitos reservados</div>
</footer>

</body>
</html>
```